KWT Website revamping

Make a website main page, navigation / menu options, couple of product pages in the 4 product categories, improvement on About us.
Our Website will need to be in PHP.
Our competitors websites for an idea.
www.morvado.example
https://heatwise.example/en-gb/brands/trovani
www.lumbra.example
www.sidra.example
Our website is temporarily hosted at https://www.brightfoldweb.example/kwt/
Once done, we would like a quote for coding the entire website as well. If we find the quote good we will go ahead with you.

Target Market(s)

Industrial and Commercial Refrigeration , Cold Store, freezer and chiller manufacturers and commercial Airconditioning contractors and Industrial Automation panel makers.

Industry/Entity Type

Engineering

Number of Pages Required

5+ page

Font styles to use
Other font styles liked:
• "Michroma" "Roboto" "MONTSERRAT"

Colors
3377b5
ffffff

Requirements
Must have
• Main page, index/menu, couple of product pages.
Nice to have
• A good navigation to the product list
Font should be similar to the top menu line
Showcase our site as a good electronics temperature controller manufacturer for Refrigeration / Industrial Process Automation

```html
<!DOCTYPE html>
<html lang="en">
<head>
<meta charset="utf-8">
<title>KWT Controls – Home</title>
<link rel="stylesheet" href="https://fonts.googleapis.com/css2?family=Michroma&family=Montserrat:wght@600;700&family=Roboto:wght@400;500;700&display=swap">
<style>
:root{
  --red:#e8353a;
  --green:#1e9b4a;
  --ink:#111;
  --text:#333;
  --muted:#777;
  --white:#fff;
  --light:#f3f3f4;
  --footer:#0b0c10;
}
*{margin:0;padding:0;box-sizing:border-box}
html,body{width:1200px;height:2594px;overflow:hidden;background:var(--white)}
body{position:relative;font-family:"Roboto",sans-serif;color:var(--text)}
.abs{position:absolute}

/* header */
.site-header{left:0;top:0;width:1200px;height:64px;background:var(--white);z-index:5}
.brand{left:235px;top:18px;display:flex;align-items:center;gap:6px;font-family:"Montserrat",sans-serif;font-weight:700;font-size:24px;color:var(--red)}
.brand-square{width:12px;height:12px;background:var(--red)}
.main-nav{left:0;top:0;width:1120px;height:64px}
.main-nav a{position:absolute;top:27px;font-family:"Michroma",sans-serif;font-size:9px;line-height:10px;color:var(--ink);text-decoration:none;white-space:nowrap}
.main-nav a.phone{color:var(--green)}
.search-box{left:1120px;top:0;width:80px;height:64px;background:var(--red)}

/* hero */
.hero{left:0;top:64px;width:1200px;height:568px;background:linear-gradient(135deg,#8c8e90 0%,#cfd1d2 40%,#e9eaea 60%,#a2a4a5 100%)}
.hero-title{left:232px;top:218px;font-family:"Montserrat",sans-serif;font-weight:700;font-size:49px;color:var(--white);letter-spacing:.5px;white-space:nowrap}
.hero-sub{left:235px;top:314px;font-family:"Montserrat",sans-serif;font-weight:700;font-size:25px;line-height:30px;color:var(--white);white-space:nowrap}
.brand-tile{top:408px;height:75px;background:var(--white);display:flex;align-items:center;justify-content:center;font-family:"Montserrat",sans-serif;font-weight:700;font-size:20px;color:var(--ink)}
.dots{left:235px;top:546px;display:flex;gap:12px}
.dots span{width:9px;height:9px;border-radius:50%;background:var(--white)}
.dots span.active{background:transparent;border:1.5px solid var(--white)}

/* headings */
.section-title{font-family:"Montserrat",sans-serif;font-weight:700;font-size:27px;color:var(--ink);white-space:nowrap}
.center{left:0;width:1200px;text-align:center}

/* about */
.about-photo{left:235px;top:718px;width:356px;height:335px;background:linear-gradient(160deg,#d9d9d9,#8f8f8f)}
.about-text{left:641px;top:806px;width:325px;font-size:10px;line-height:18.8px;color:var(--text)}
.btn-more{left:641px;top:994px;width:100px;height:36px;background:var(--green);color:var(--white);font-size:10px;font-weight:700;display:flex;align-items:center;justify-content:center;clip-path:polygon(0 0,88% 0,100% 28%,100% 100%,0 100%)}

.circuit{left:0;width:1200px;background:linear-gradient(180deg,rgba(230,231,233,0) 0%,rgba(215,217,220,.55) 100%)}

/* products */
.products-bg{left:0;top:1150px;width:1200px;height:556px;background:linear-gradient(120deg,#e9eaeb,#f4f4f5 50%,#e2e3e4);clip-path:polygon(0 12%,8% 0,92% 0,100% 12%,100% 100%,0 100%)}
.tagline{top:1368px;font-family:"Michroma",sans-serif;font-size:10px;color:var(--ink);letter-spacing:-.3px;white-space:nowrap}
.product-card{top:1426px;width:169px}
.product-photo{height:171px}
.product-name{margin-top:26px;text-align:center;font-size:11.5px;font-weight:700;letter-spacing:.5px;color:var(--ink);white-space:nowrap}

/* events */
.event-card{top:1864px;width:231px;height:236px}
.event-logo{position:absolute;left:0;top:0;width:231px;height:200px;background:var(--light)}
.event-logo-fill{position:absolute;left:0;top:0;width:231px;height:166px;display:flex;align-items:center;justify-content:center;font-family:"Montserrat",sans-serif;font-weight:700;font-size:18px;color:#2a5fa8;white-space:nowrap}
.event-info{position:absolute;left:0;top:166px;width:203px;height:70px;background:var(--white);padding:14px 0 0 22px}
.event-date{font-size:9px;color:var(--muted);font-weight:500;white-space:nowrap}
.event-venue{margin-top:12px;border-left:2px solid var(--green);padding-left:11px;font-size:9px;font-weight:700;line-height:19px;color:var(--ink);white-space:nowrap}

/* footer */
.site-footer{left:0;top:2240px;width:1200px;height:354px;background:var(--footer)}
.foot-brands{left:270px;top:2305px;display:flex;gap:12px;font-family:"Montserrat",sans-serif;font-weight:700;font-size:13px;color:var(--white)}
.foot-badge{left:309px;top:2332px;width:44px;height:44px;border-radius:50%;background:#c9342f}
.foot-col{top:2300px;color:#c9c9cc;font-size:9px}
.foot-col h4{font-size:10px;font-weight:500;color:var(--white);margin-bottom:15px;letter-spacing:.3px;white-space:nowrap}
.foot-col li{list-style:none;height:20px;display:flex;align-items:flex-start;gap:10px;white-space:nowrap}
.connect li{height:25px}
.ico{width:7px;height:7px;border-radius:50%;background:#9a9aa0;margin-top:2px;flex:none}
.location p{line-height:16px}
.loc-row{display:flex;gap:9px;margin-bottom:8px}
.copyright{top:2486px;font-size:9px;color:#c9c9cc}
.legal{top:2512px;font-size:9px;color:#c9c9cc}
.wave{left:0;top:2535px;width:1200px;height:59px;background:linear-gradient(180deg,rgba(11,12,16,0),rgba(60,90,110,.45))}
</style>
</head>
<body>

<header class="site-header abs">
  <div class="brand abs"><span class="brand-square"></span>KWT</div>
  <nav class="main-nav abs">
    <a style="left:375px">HOME</a>
    <a style="left:450px">ABOUT US</a>
    <a style="left:550px">PRODUCT</a>
    <a style="left:648px">RESOURCES</a>
    <a style="left:761px">HIGHLIGHTS</a>
    <a style="left:870px">CONTACT</a>
    <a class="phone" style="left:964px">+91-22-40001234</a>
  </nav>
  <div class="search-box abs">
    <svg width="80" height="64" viewBox="0 0 80 64"><circle cx="38" cy="30" r="6" fill="none" stroke="#fff" stroke-width="2"/><line x1="42.5" y1="34.5" x2="47" y2="39" stroke="#fff" stroke-width="2.2" stroke-linecap="round"/></svg>
  </div>
</header>

<section class="hero abs" role="img" aria-label="Stainless steel cold room interior with overhead lighting"></section>
<svg class="abs" style="left:0;top:540px" width="1200" height="95" viewBox="0 0 1200 95">
  <polygon points="0,13 135,92 0,92" fill="#fff"/>
  <polygon points="1200,13 1065,92 1200,92" fill="#fff"/>
  <polygon points="0,92 1200,92 1200,95 0,95" fill="#fff"/>
  <line x1="0" y1="13" x2="112" y2="75" stroke="#e8353a" stroke-width="4"/>
  <circle cx="112" cy="75" r="6" fill="#e8353a"/>
  <line x1="1200" y1="13" x2="1092" y2="75" stroke="#e8353a" stroke-width="4"/>
  <circle cx="1092" cy="75" r="6" fill="#e8353a"/>
</svg>
<h1 class="hero-title abs">REFRIGERATION</h1>
<svg class="abs" style="left:234px;top:283px" width="135" height="10"><line x1="0" y1="5" x2="128" y2="5" stroke="#fff" stroke-width="1.5"/><circle cx="128" cy="5" r="4" fill="#fff"/></svg>
<p class="hero-sub abs">SUPPLYING INDIA WITH<br>ADVANCED COOLING SOLUTIONS</p>
<div class="brand-tile abs" style="left:235px;width:142px">FORTEN</div>
<div class="brand-tile abs" style="left:390px;width:124px">POLARO</div>
<div class="dots abs"><span class="active"></span><span></span><span></span></div>

<section class="about">
  <div class="about-photo abs" role="img" aria-label="Technician operating a controller assembly machine"></div>
  <h2 class="section-title abs" style="left:643px;top:733px">ABOUT US</h2>
  <svg class="abs" style="left:643px;top:771px" width="65" height="10"><line x1="0" y1="5" x2="56" y2="5" stroke="#e8353a" stroke-width="1.5"/><circle cx="56" cy="5" r="4" fill="#e8353a"/></svg>
  <p class="about-text abs">R.N. Controls Pvt. Ltd. was established in 1986, and started out as a small manufacturing unit that developed level controls and valves for ammonia plants. Today our technical innovation puts us in the forefront of the Refrigeration and Air-Conditioning control industry in India. We have two established brands – Forten and Polaro, both of which have grabbed the attention, and the loyalty of several industry leaders. What is impressive is the vast array of products from mechanical components to automation to humidification and temperature controls. The 20 year old POLARO brand is widely accepted pan India.</p>
  <a class="btn-more abs">READ MORE</a>
</section>

<div class="circuit abs" style="top:970px;height:255px" role="img" aria-label="Faint circuit trace pattern"></div>

<section class="products">
  <div class="products-bg abs" role="img" aria-label="Faded industrial machinery backdrop"></div>
  <h2 class="section-title abs center" style="top:1288px">OUR PRODUCTS</h2>
  <svg class="abs" style="left:566px;top:1331px" width="68" height="12"><line x1="6" y1="6" x2="62" y2="6" stroke="#e8353a" stroke-width="1.5"/><circle cx="6" cy="6" r="4" fill="#e8353a"/><circle cx="62" cy="6" r="4" fill="#e8353a"/></svg>
  <p class="tagline abs center">THE WIDEST RANGE OF HVAC&amp;R AND PROCESS CONTROL INSTRUMENTATION.</p>
  <div class="product-card abs" style="left:235px"><div class="product-photo" role="img" aria-label="Cold storage warehouse with stacked boxes" style="background:linear-gradient(180deg,#e8e6e2,#b9a58c)"></div><p class="product-name">HVAC&amp;R CONTROLLERS</p></div>
  <div class="product-card abs" style="left:422px"><div class="product-photo" role="img" aria-label="Stainless steel processing room" style="background:linear-gradient(180deg,#c9cdd0,#8d9296)"></div><p class="product-name">HVACR ELECTRICAL PANELS</p></div>
  <div class="product-card abs" style="left:609px"><div class="product-photo" role="img" aria-label="Bottling line in an automated plant" style="background:linear-gradient(180deg,#3f6fb0 0%,#1d3f7a 60%,#e7a615 85%,#1d3f7a 100%)"></div><p class="product-name">INDUSTRIAL AUTOMATION</p></div>
  <div class="product-card abs" style="left:797px"><div class="product-photo" role="img" aria-label="Industrial pipework and valves" style="background:linear-gradient(120deg,#8fb0d6,#2d4f7d 55%,#6d8fb8)"></div><p class="product-name">VALVES &amp; CONTROLS</p></div>
</section>

<section class="events">
  <h2 class="section-title abs center" style="top:1770px">EVENTS</h2>
  <svg class="abs" style="left:566px;top:1812px" width="68" height="12"><line x1="6" y1="6" x2="62" y2="6" stroke="#e8353a" stroke-width="1.5"/><circle cx="6" cy="6" r="4" fill="#e8353a"/><circle cx="62" cy="6" r="4" fill="#e8353a"/></svg>

  <article class="event-card abs" style="left:235px">
    <div class="event-logo"></div><div class="event-logo-fill">Climex Show 2021</div>
    <div class="event-info"><p class="event-date">25th to 27th February 2021</p><p class="event-venue">LAKESIDE EXHIBITION<br>CENTRE, BENGALURU</p></div>
  </article>
  <article class="event-card abs" style="left:485px">
    <div class="event-logo"></div><div class="event-logo-fill">Autoworks Expo 2021</div>
    <div class="event-info"><p class="event-date">22nd to 25th September 2021</p><p class="event-venue">HARBOUR EXPO CENTRE, MUMBAI<br>Visit us at : Stall No. I-20 to I-23</p></div>
  </article>
  <article class="event-card abs" style="left:735px">
    <div class="event-logo"></div><div class="event-logo-fill">Coldline Fair</div>
    <div class="event-info"><p class="event-date">29th to 31st October 2020</p><p class="event-venue">CAPITAL EXPO CENTRE &amp; MART,<br>NEW DELHI, INDIA</p></div>
  </article>
</section>

<div class="circuit abs" style="top:2140px;height:100px" role="img" aria-label="Faint circuit trace pattern"></div>

<footer class="site-footer abs">
</footer>
<svg class="abs" style="left:0;top:2240px" width="1200" height="80" viewBox="0 0 1200 80">
  <polygon points="0,0 135,0 0,78" fill="#fff"/>
  <polygon points="1200,0 1065,0 1200,78" fill="#fff"/>
  <line x1="0" y1="77" x2="110" y2="13" stroke="#e8353a" stroke-width="4"/>
  <circle cx="110" cy="13" r="6" fill="#e8353a"/>
  <line x1="1200" y1="77" x2="1090" y2="13" stroke="#e8353a" stroke-width="4"/>
  <circle cx="1090" cy="13" r="6" fill="#e8353a"/>
</svg>
<div class="foot-brands abs"><span>POLARO</span><span>FORTEN</span></div>
<div class="foot-badge abs"></div>

<div class="foot-col abs" style="left:461px">
  <h4>QUICK LINKS</h4>
  <ul><li>About Us</li><li>Products</li><li>Career</li><li>Gallery</li><li>Contact</li></ul>
</div>
<div class="foot-col connect abs" style="left:593px">
  <h4>CONNECT US</h4>
  <ul><li><span class="ico"></span>Facenet</li><li><span class="ico"></span>Chirper</li><li><span class="ico"></span>Viewtube</li><li><span class="ico"></span>Snapgram</li></ul>
</div>
<div class="foot-col location abs" style="left:733px;width:210px">
  <h4>LOCATION</h4>
  <div class="loc-row">
    <svg width="8" height="11" viewBox="0 0 8 11" style="flex:none;margin-top:2px"><path d="M4 0a4 4 0 0 1 4 4c0 3-4 7-4 7S0 7 0 4a4 4 0 0 1 4-4z" fill="#9a9aa0"/><circle cx="4" cy="4" r="1.5" fill="#0b0c10"/></svg>
    <p>B-42, Riverside Industrial Estate, Sector 9, Harbour Road, New Bombay – 400 999, INDIA.</p>
  </div>
  <div class="loc-row">
    <svg width="9" height="9" viewBox="0 0 9 9" style="flex:none;margin-top:3px"><path d="M1 0h2l1 2.5-1.2 1a5 5 0 0 0 2.7 2.7l1-1.2L9 6v2a1 1 0 0 1-1 1A8 8 0 0 1 0 1a1 1 0 0 1 1-1z" fill="#9a9aa0"/></svg>
    <p>+91-22-40001234</p>
  </div>
  <div class="loc-row">
    <svg width="9" height="8" viewBox="0 0 9 8" style="flex:none;margin-top:4px"><rect width="9" height="7" fill="#9a9aa0"/><path d="M0 0l4.5 3.5L9 0" stroke="#0b0c10" fill="none"/></svg>
    <p>sales@kwtcontrols.example</p>
  </div>
</div>

<p class="copyright abs center">KWT CONTROLS © 2020. All Rights Reserved. Developed By Brightfold Web Studio</p>
<p class="legal abs center">Site Map &nbsp;|&nbsp; About &nbsp;|&nbsp; Privacy Policy</p>
<div class="wave abs" role="img" aria-label="Wireframe terrain graphic"></div>

</body>
</html>
```